Check, Perfect and Polish my Perfume Brochure

I will send my brochure to stores that sell perfumes.
The perfumes stores are located all around the world.

In this brochure/booklet I will tell the stores about my
1. my life
2. How I made perfumes on my own
3. I will talk about the perfumes I sell

I will use this brochure/booklet to make connections with perfume stores.
They should know, and remember who I am from this booklet.
I will use this brochure/booklet to make sales.

I need a graphic designer with
1. print experience
2. booklet and brochure making experience
3. very detailed eyes
4. good spelling
5. experience in fashion, health beauty products is important
6. please help me edit and polishing my brochure
7. my brochure to look very professional

This is the main point, to help me make my brochure look very cool, fashionable and professional

Target Market(s)

Perfume Store

Industry/Entity Type

perfumery, fashion, boutiques, high end luxury

Font styles to use
Serif

Colors
FFC000
F8CF3A
FAE287
FDF2CF
FEFAEE

Requirements
Must have
• 1. consistent design on all pages 2. have consistent colour and fonts 3. attractive photos 4. tell the stores about my brand 5. tell the stores about my life 6. tell the stores why my perfumes are very good
Nice to have
• I will like to have your personal style and suggestions please

```html
<!DOCTYPE html>
<html lang="en">
<head>
<meta charset="utf-8">
<title>Verane Handmade Perfumes – Brochure Cover</title>
<link rel="stylesheet" href="https://fonts.googleapis.com/css2?family=Marcellus&family=Playfair+Display:wght@400&display=swap">
<style>
  :root {
    --paper: #ffffff;
    --cocoa: #5e4037;
    --espresso: #4a2418;
    --ink: #1a1a1a;
    --rust: #8a4a33;
    --amber: #f29a2e;
    --amber-light: #f7b24a;
    --cream: #ffffff;
  }
  * { margin: 0; padding: 0; box-sizing: border-box; }
  html, body {
    width: 1200px;
    height: 768px;
    overflow: hidden;
    background: var(--paper);
  }
  .cover {
    position: relative;
    width: 1200px;
    height: 768px;
    background: var(--paper);
    overflow: hidden;
  }
  .cover-art {
    position: absolute;
    inset: 0;
    width: 1200px;
    height: 768px;
  }
  .arc-title {
    font-family: "Marcellus", serif;
    font-size: 62px;
    letter-spacing: 6px;
    fill: var(--espresso);
  }
  .brand-name {
    font-family: "Marcellus", serif;
    font-size: 46px;
    letter-spacing: 4px;
    fill: var(--ink);
  }
  .brand-tagline {
    font-family: "Marcellus", serif;
    font-size: 13px;
    letter-spacing: 2px;
    fill: var(--ink);
  }
  .headline {
    position: absolute;
    left: 0;
    width: 1200px;
    top: 528px;
    padding-left: 2px;
    text-align: center;
    font-family: "Marcellus", serif;
    font-weight: 400;
    font-size: 114px;
    line-height: 1;
    letter-spacing: 1px;
    color: var(--cream);
  }
  .web-row {
    position: absolute;
    top: 678px;
    left: 0;
    width: 1200px;
    height: 55px;
  }
  .web-rule {
    position: absolute;
    top: 27px;
    height: 2px;
    background: var(--amber);
  }
  .web-rule--left { left: 160px; width: 170px; }
  .web-rule--right { left: 842px; width: 170px; }
  .web-flourish {
    position: absolute;
    top: 19px;
    width: 100px;
    height: 18px;
    border-radius: 9px;
    background: linear-gradient(90deg, var(--amber-light), var(--amber));
  }
  .web-flourish--left { left: 156px; }
  .web-flourish--right { left: 914px; }
  .web-pill {
    position: absolute;
    left: 326px;
    top: 0;
    width: 520px;
    height: 55px;
    border: 2px solid var(--amber);
    border-radius: 28px;
    background: var(--rust);
    display: flex;
    align-items: center;
    justify-content: center;
    font-family: "Playfair Display", serif;
    font-size: 33px;
    letter-spacing: 3px;
    color: var(--cream);
  }
</style>
</head>
<body>
<main class="cover">
  <svg class="cover-art" viewBox="0 0 1200 768" xmlns="http://www.w3.org/2000/svg">
    <defs>
      <path id="handcraft-arc" d="M398,300 A194,194 0 0 1 782,300"/>
    </defs>

    <path class="floral-band" role="img" aria-label="Brown band filled with a hand-drawn pattern of roses and daisies"
      fill="#5e4037"
      d="M0,362
         c10,0 12,-12 25,-12 c13,0 15,12 25,12 c10,0 12,-12 25,-12 c13,0 15,12 25,12
         c10,0 12,-12 25,-12 c13,0 15,12 25,12 c10,0 12,-12 25,-12 c13,0 15,12 25,12
         c10,0 12,-12 25,-12 c13,0 15,12 25,12 c10,0 12,-12 25,-12 c13,0 15,12 25,12
         c10,0 12,-12 25,-12 c13,0 15,12 25,12 c10,0 12,-12 25,-12 c13,0 15,12 25,12
         c10,0 12,-12 25,-12 c13,0 15,12 25,12 c10,0 12,-12 25,-12 c13,0 15,12 25,12
         c10,0 12,-12 25,-12 c13,0 15,12 25,12 c10,0 12,-12 25,-12 c13,0 15,12 25,12
         c10,0 12,-12 25,-12 c13,0 15,12 25,12 c10,0 12,-12 25,-12 c13,0 15,12 25,12
         c10,0 12,-12 25,-12 c13,0 15,12 25,12 c10,0 12,-12 25,-12 c13,0 15,12 25,12
         c10,0 12,-12 25,-12 c13,0 15,12 25,12 c10,0 12,-12 25,-12 c13,0 15,12 25,12
         c10,0 12,-12 25,-12 c13,0 15,12 25,12 c10,0 12,-12 25,-12 c13,0 15,12 25,12
         c10,0 12,-12 25,-12 c13,0 15,12 25,12 c10,0 12,-12 25,-12 c13,0 15,12 25,12
         c10,0 12,-12 25,-12 c13,0 15,12 25,12 c10,0 12,-12 25,-12 c13,0 15,12 25,12
         L1200,768 L0,768 Z"/>

    <path class="arc-rule" d="M414,300 A182,182 0 0 0 408,352" fill="none" stroke="#4a2418" stroke-width="1.2"/>
    <path class="arc-rule" d="M766,300 A182,182 0 0 1 772,352" fill="none" stroke="#4a2418" stroke-width="1.2"/>

    <text class="arc-title">
      <textPath href="#handcraft-arc" startOffset="50%" text-anchor="middle">HANDCRAFT</textPath>
    </text>

    <circle class="brand-disc" cx="590" cy="342" r="132" fill="#ffffff"/>
    <text class="brand-name" x="590" y="358" text-anchor="middle">VERANE</text>
    <text class="brand-tagline" x="590" y="390" text-anchor="middle">HANDMADE PERFUMES</text>
  </svg>

  <h1 class="headline">PERFUMES</h1>

  <div class="web-row">
    <span class="web-rule web-rule--left"></span>
    <span class="web-flourish web-flourish--left" role="img" aria-label="Amber scroll ornament"></span>
    <span class="web-rule web-rule--right"></span>
    <span class="web-flourish web-flourish--right" role="img" aria-label="Amber scroll ornament"></span>
    <p class="web-pill">www.veraneperfumes.com</p>
  </div>
</main>
</body>
</html>
```